DJTarnish.net

A clean-looking fun website.

MAP*

top* Video. (To host party footage and also to host live streams as they happen.

Tabs - Events, Livestream, Mixes, Playlists, Sign up, Photos, Bio, Shop

Links to Pixo, Facet and Chirp, Tubely & Twitch

sign up sheet to take contact details for future promo.

References
http://www.djbrindlemoss.net/
http://www.rexhollowbay.net/
https://blunkerdrave.net/
https://www.djorvanpeltsite.net/
https://nedbrisk.net/
https://www.amosvantry.net/bed/

I hope this helps.

```html
<!DOCTYPE html>
<html lang="en">
<head>
<meta charset="utf-8">
<title>DJ Tarnish — DJ and Live Stream Entertainment</title>
<link rel="stylesheet" href="https://fonts.googleapis.com/css2?family=Montserrat:wght@400;500;600;700;800;900&family=Poppins:wght@400;500;600;700&display=swap">
<style>
:root{
  --black:#000;
  --ink:#0a0a0a;
  --panel:#1f1f22;
  --panel-dark:#151517;
  --white:#fff;
  --muted:#bdbdbd;
  --dim:#6f6f6f;
  --red:#e5141b;
  --orange:#d9782c;
  --stage:#f4f4f4;
}
*{margin:0;padding:0;box-sizing:border-box}
html,body{width:1200px;height:4261px;overflow:hidden}
body{background:var(--stage);font-family:"Montserrat",sans-serif;color:var(--white)}
.page{position:absolute;left:157px;top:53px;width:895px;height:4189px;background:var(--black);overflow:hidden}
.abs{position:absolute}
.media{position:absolute}
.h-section{font-family:"Poppins",sans-serif;font-weight:600;font-size:30px;text-align:center;left:0;width:895px}
.rule{position:absolute;height:3px;background:var(--white);width:68px}
.copy{font-size:7.4px;line-height:12.6px;color:#e2e2e2}
.pill{position:absolute;background:var(--white);color:var(--black);border-radius:16px;font-size:7.5px;font-weight:700;display:flex;align-items:center;justify-content:center;letter-spacing:.3px}
.social{display:flex;gap:10px;align-items:center}
.social span{font-size:8px;font-weight:500;display:flex;align-items:center;gap:3px}
.social span::before{content:"";width:6px;height:6px;border-radius:50%;border:1.3px solid currentColor}

/* hero */
.hero{left:0;top:0;width:895px;height:522px}
.hero-photo{inset:0;background:
  radial-gradient(ellipse 340px 300px at 620px 230px,#e08a3c 0%,#a6521f 35%,rgba(60,25,10,.6) 70%,transparent 100%),
  radial-gradient(ellipse 260px 200px at 150px 320px,#8a4418 0%,transparent 100%),
  linear-gradient(180deg,#6b3214 0%,#3a1a0a 60%,#000 100%)}
.logo{left:43px;top:16px;font-family:"Montserrat",sans-serif;font-weight:900;font-size:30px;letter-spacing:-.5px;display:flex;align-items:center;gap:8px}
.logo i{width:14px;height:14px;background:var(--white);display:block}
.nav{left:237px;top:29px;display:flex;gap:27px;font-size:8px}
.hero .social{left:757px;top:30px}
.hero-title{left:40px;top:182px;font-weight:800;font-size:32px;line-height:36px;letter-spacing:.5px}
.hero-sub{left:43px;top:268px;font-size:8px;color:#f3d9c4}
.btn-outline{left:43px;top:303px;width:109px;height:24px;border:1.5px solid var(--white);font-size:7px;display:flex;align-items:center;justify-content:center}
.play{left:182px;top:290px}
.today{left:108px;top:400px;font-size:6.5px;color:#ddd;transform:rotate(-90deg);transform-origin:left top;letter-spacing:1px}
.today-line{left:113px;top:405px;width:1px;height:80px;background:#e9a35c}

/* biography */
.bio-title{left:57px;top:610px;font-family:"Poppins",sans-serif;font-weight:600;font-size:32px}
.bio-copy{left:57px;top:675px;width:310px}
.bio-copy p{margin-bottom:12px}
.bio-btn{left:62px;top:845px;width:98px;height:27px}
.bio-photo{left:445px;top:605px;width:392px;height:260px;background:linear-gradient(160deg,#d8d8d8 0%,#7a7a7a 40%,#2a2a2a 100%)}

/* events */
.tabs{left:170px;top:1056px;width:560px;display:flex;justify-content:space-between;font-size:7px;color:var(--dim);padding:0 42px 0 42px}
.tabs .active{color:var(--white);font-weight:600}
.tab-line{left:170px;top:1083px;width:560px;height:1px;background:#3a3a3a}
.tab-active{left:170px;top:1082px;width:132px;height:3px;background:var(--white)}
.event-photo{left:50px;top:1147px;width:407px;height:293px;background:radial-gradient(ellipse at 40% 30%,#3a40d8 0%,#c5152f 45%,#4a0818 100%)}
.arrows{left:395px;top:1414px;display:flex;gap:3px}
.arrows span{width:27px;height:25px;background:var(--white);display:flex;align-items:center;justify-content:center}
.event-title{left:505px;top:1143px;font-weight:700;font-size:16px}
.event-copy{left:505px;top:1180px;width:330px}
.event-copy p{margin-bottom:12px}
.share{left:505px;top:1360px;font-size:6px;font-weight:700;letter-spacing:.5px}
.event-social{left:505px;top:1378px}
.event-btn{left:503px;top:1410px;width:130px;height:30px}

/* live stream */
.stream-bg{left:0;top:1490px;width:895px;height:505px;background:
  radial-gradient(ellipse 420px 170px at 447px 60px,#4c4c52 0%,#17171a 60%,#000 100%)}
.stream-panel{left:77px;top:1610px;width:758px;height:323px;background:var(--panel);border-radius:4px}
.stream-card{left:128px;top:1635px;width:187px;height:273px;background:var(--ink);border-radius:4px}
.stream-card h3{position:absolute;left:15px;top:58px;font-weight:400;font-size:16px;line-height:18px}
.stream-card .label{position:absolute;left:15px;top:130px;font-size:9px;font-weight:600}
.stream-card .field{position:absolute;left:15px;top:163px;width:120px;height:24px;background:#e6e6e6}
.stream-card .join{position:absolute;left:18px;top:199px;font-size:7px;color:#aaa}
.stream-video{left:360px;top:1625px;width:428px;height:292px;border-radius:4px;background:radial-gradient(ellipse 140px 90px at 214px 120px,#a8a39a 0%,#3d3b38 45%,#101012 100%)}

/* playlist */
.player{left:68px;top:2113px;width:429px;height:284px;background:linear-gradient(90deg,#3b3b3b 0%,#8b7a6c 45%,#2a2523 100%)}
.song-title{left:68px;top:2232px;width:429px;text-align:center;font-family:"Poppins",sans-serif;font-weight:600;font-size:21px}
.times{left:138px;top:2330px;width:255px;display:flex;justify-content:space-between;font-size:6.5px}
.bar{left:138px;top:2343px;width:255px;height:4px;background:#d8d8d8}
.bar i{display:block;width:133px;height:4px;background:var(--red)}
.controls{left:138px;top:2357px;width:255px;display:flex;justify-content:space-between;align-items:center}
.latest{left:560px;top:2094px;font-size:11px;font-weight:500}
.latest-line{left:552px;top:2116px;width:140px;height:1px;background:#777}
.songs{left:552px;top:2138px;width:228px}
.song{position:relative;height:57px;margin-bottom:10px;background:var(--white);color:var(--black)}
.song .name{position:absolute;left:9px;top:10px;font-size:7px}
.song .dur{position:absolute;left:9px;top:28px;font-size:7px;display:flex;align-items:center;gap:8px}
.song .thumb{position:absolute;right:0;top:0;width:83px;height:57px}
.scroll{left:811px;top:2133px;width:2px;height:260px;background:#3a3a3a}
.scroll i{display:block;height:35px;background:var(--red)}

/* mix */
.mix-art{left:27px;top:2480px;width:400px;height:350px;background:radial-gradient(ellipse at 55% 50%,#3c6fa8 0%,#382a55 40%,#000 75%)}
.mix-title{left:492px;top:2525px;font-family:"Poppins",sans-serif;font-weight:600;font-size:28px}
.mix-rule{left:492px;top:2567px;width:45px}
.mix-copy{left:492px;top:2588px;width:290px}
.mix-copy p{margin-bottom:12px}

/* photos */
.photos-bg{left:0;top:2880px;width:895px;height:525px;background:linear-gradient(180deg,#000 0%,#5a2220 25%,#4a1d1c 75%,#000 100%)}
.photo{position:absolute}

/* shop */
.view-all{left:728px;top:3498px;font-size:9px;font-weight:600;display:flex;align-items:center;gap:8px}
.shirt{position:absolute;top:3522px;width:145px;height:183px}
.buy{position:absolute;top:3733px;display:flex;gap:8px}
.cart{width:31px;height:27px;background:var(--red);display:flex;align-items:center;justify-content:center}
.buy b{display:block;font-size:8px;font-weight:700;margin-top:3px}
.buy small{display:block;font-size:6.5px;margin-top:3px}

/* newsletter */
.newsletter{left:0;top:3860px;width:895px;height:150px;background:var(--white);color:var(--black)}
.newsletter .join{position:absolute;left:60px;top:40px;font-family:"Poppins",sans-serif;font-size:20px;font-weight:500}
.newsletter .big{position:absolute;left:60px;top:63px;font-family:"Poppins",sans-serif;font-size:31px;font-weight:700}
.email{position:absolute;left:352px;top:50px;width:361px;height:50px;background:#efefef;font-size:14px;font-weight:600;display:flex;align-items:center;padding-left:17px;color:#111}
.submit{position:absolute;left:713px;top:50px;width:102px;height:50px;background:var(--red);color:var(--white);font-size:15px;font-weight:700;display:flex;align-items:center;justify-content:center}

/* footer */
.foot-nav{left:0;top:4078px;width:895px;display:flex;justify-content:center;gap:14px;font-family:"Poppins",sans-serif;font-size:16px}
.foot-nav .gap{margin-left:14px}
.foot-line{left:160px;top:4122px;width:575px;height:1px;background:#555}
.copyright{left:0;top:4133px;width:895px;text-align:center;font-size:7px;color:#bbb}
.foot-social{left:0;top:4157px;width:895px;justify-content:center}
</style>
</head>
<body>
<main class="page">

  <!-- hero -->
  <section class="abs hero">
    <div class="media hero-photo" role="img" aria-label="DJ singing into a microphone with headphones, warm orange stage light"></div>
    <div class="abs logo"><i></i>Tarnish</div>
    <nav class="abs nav"><span>Events</span><span>Livestream</span><span>Mixes</span><span>Playlists</span><span>Sign up</span><span>Photos</span><span>Bio</span><span>Shop</span></nav>
    <div class="abs social"><span>Pixo</span><span>Facet</span><span>Tubely</span><span>Chirp</span></div>
    <h1 class="abs hero-title">DJ AND LIVE<br>STREAM ENTERTAINMENT</h1>
    <p class="abs hero-sub">Lorem ipsum dolor sit amet, consectetur adipiscing elit.</p>
    <div class="abs btn-outline">Enter to the Stream</div>
    <svg class="abs play" width="52" height="52" viewBox="0 0 52 52"><circle cx="26" cy="26" r="24" fill="none" stroke="#fff" stroke-width="2.5"/><path d="M20 15 L37 26 L20 37 Z" fill="#fff"/></svg>
    <span class="abs today">TODAY</span>
    <span class="abs today-line"></span>
  </section>

  <!-- biography -->
  <section>
    <h2 class="abs bio-title">Biography</h2>
    <span class="rule" style="left:57px;top:662px;width:90px"></span>
    <div class="abs copy bio-copy">
      <p>Lorem ipsum dolor sit amet, consectetur adipiscing elit. Molestie scelerisque volutpat consectetur laoreet purus fermentum commodo, nullam vulputate. Praesent lorem elementum ac aliquet. Arcu vulputate urna bibendum elementum cursus suscipit nunc faucibus posuere. Convallis neque amet fermentum sed. Porttitor nibh amet pretium suscipit dapibus consequat tincidunt. Sit nunc, felis cursus adipiscing posuere vulputate.</p>
      <p>Auctor mauris orci fusce tortor, velit, non tellus. Risus, nisl aliquet aenean et maecenas sed urna nulla. Imperdiet habitant convallis sit augue.</p>
      <p>Auctor mauris orci fusce tortor, velit, non tellus. Risus, nisl aliquet aenean et maecenas sed urna nulla. Imperdiet habitant convallis sit augue.</p>
    </div>
    <div class="pill bio-btn">READ MORE</div>
    <div class="media bio-photo" role="img" aria-label="Black and white photo of a DJ crew on a crowded balcony stage"></div>
  </section>

  <!-- events -->
  <section>
    <h2 class="abs h-section" style="top:950px">Events</h2>
    <span class="rule" style="left:412px;top:995px"></span>
    <div class="abs tabs"><span class="active">Night Parties</span><span>Beach Parties</span><span>Farmhouse Parties</span><span>Road Parties</span></div>
    <span class="abs tab-line"></span>
    <span class="abs tab-active"></span>
    <div class="media event-photo" role="img" aria-label="DJ with headphones at the decks under red and blue club lights"></div>
    <div class="abs arrows">
      <span><svg width="10" height="10" viewBox="0 0 10 10"><rect x="0" y="0" width="10" height="10" fill="#000"/><path d="M6.5 2 L3 5 L6.5 8" stroke="#fff" stroke-width="1.4" fill="none"/></svg></span>
      <span><svg width="10" height="10" viewBox="0 0 10 10"><rect x="0" y="0" width="10" height="10" fill="#000"/><path d="M3.5 2 L7 5 L3.5 8" stroke="#fff" stroke-width="1.4" fill="none"/></svg></span>
    </div>
    <h3 class="abs event-title">Night party</h3>
    <div class="abs copy event-copy">
      <p>Lorem ipsum dolor sit amet, consectetur adipiscing elit. Viverra eu cursus et tellus suscipit. A fames urna, mattis diam. Aliquam placerat lacus augue leo interdum id amet fringilla. Tempor sem purus pellentesque proin semper. Eget morbi odio donec pellentesque. Id vitae sit cras id sit. Nunc, quis dictumst non tellus posuere. Lorem ipsum dolor sit amet, consectetur adipiscing elit. Viverra eu cursus et tellus suscipit. A fames urna, mattis diam.</p>
      <p>Lorem ipsum dolor sit amet, consectetur adipiscing elit. Viverra eu cursus et tellus suscipit. A fames urna, mattis diam. Aliquam placerat lacus augue leo interdum id amet fringilla. Tempor sem purus pellentesque proin semper. Eget morbi odio donec pellentesque. Id vitae sit cras id sit. Nunc, quis dictumst non tellus posuere. Lorem ipsum dolor sit amet, consectetur adipiscing elit. Viverra eu cursus et tellus suscipit. A fames urna, mattis diam.</p>
    </div>
    <span class="abs share">SHARE IT:</span>
    <div class="abs social event-social"><span>Pixo</span><span>Facet</span><span>Chirp</span></div>
    <div class="pill event-btn">SEE OUR LAST EVENT</div>
  </section>

  <!-- live stream -->
  <section>
    <div class="media stream-bg" role="img" aria-label="Concert stage with white light beams and crowd silhouettes"></div>
    <h2 class="abs h-section" style="top:1512px">Live Stream</h2>
    <span class="rule" style="left:412px;top:1562px;width:80px"></span>
    <div class="abs stream-panel"></div>
    <div class="abs stream-card">
      <h3>write your<br>id to enter<br>the stream</h3>
      <span class="label">Enter ID</span>
      <span class="field"></span>
      <span class="join">JOIN</span>
    </div>
    <div class="media stream-video" role="img" aria-label="Live stream video of a crowd with raised hands in front of a lit stage"></div>
    <svg class="abs" style="left:540px;top:1724px" width="96" height="96" viewBox="0 0 96 96"><circle cx="48" cy="48" r="44" fill="none" stroke="#fff" stroke-width="5"/><path d="M38 28 L68 48 L38 68 Z" fill="#fff"/></svg>
  </section>

  <!-- playlist -->
  <section>
    <h2 class="abs h-section" style="top:1983px">Playlist</h2>
    <span class="rule" style="left:412px;top:2031px"></span>
    <div class="media player" role="img" aria-label="Singer with long hair holding a microphone stand"></div>
    <p class="abs song-title">It’s Not Easy</p>
    <div class="abs times"><span>2:35</span><span>6:05</span></div>
    <div class="abs bar"><i></i></div>
    <div class="abs controls">
      <svg width="60" height="12" viewBox="0 0 60 12" fill="#fff"><path d="M8 1 L2 6 L8 11 Z M14 1 L8 6 L14 11 Z"/><path d="M26 1 L34 6 L26 11 Z"/><path d="M42 1 L48 6 L42 11 Z M48 1 L54 6 L48 11 Z"/></svg>
      <svg width="80" height="12" viewBox="0 0 80 12" fill="none" stroke="#fff" stroke-width="1.2"><path d="M2 3 H10 L8 1 M10 9 H2 L4 11"/><path d="M24 4 A4 4 0 1 1 24 9 M24 4 L22 2"/><path d="M44 4 H47 L51 1 V11 L47 8 H44 Z" fill="#fff"/><rect x="66" y="2" width="9" height="8" fill="#fff"/></svg>
    </div>
    <p class="abs latest">Latest Songs</p>
    <span class="abs latest-line"></span>
    <div class="abs songs">
      <div class="song"><span class="name">Lorem ipsum dolor</span><span class="dur"><svg width="9" height="10"><path d="M0 0 L9 5 L0 10 Z" fill="#000"/></svg>6:05</span><span class="media thumb" role="img" aria-label="Singer on a magenta-lit stage" style="background:linear-gradient(135deg,#e0409a,#5a1a6a)"></span></div>
      <div class="song"><span class="name">Lorem ipsum dolor</span><span class="dur"><svg width="9" height="10"><path d="M0 0 L9 5 L0 10 Z" fill="#000"/></svg>3:25</span><span class="media thumb" role="img" aria-label="Performer under blue stage lights" style="background:linear-gradient(135deg,#3a3ad8,#1a1040)"></span></div>
      <div class="song"><span class="name">Lorem ipsum dolor</span><span class="dur"><svg width="9" height="10"><path d="M0 0 L9 5 L0 10 Z" fill="#000"/></svg>4:58</span><span class="media thumb" role="img" aria-label="Singer in pink and purple light" style="background:linear-gradient(135deg,#d04fa0,#6a2a8a)"></span></div>
      <div class="song"><span class="name">Lorem ipsum dolor</span><span class="dur"><svg width="9" height="10"><path d="M0 0 L9 5 L0 10 Z" fill="#000"/></svg>3:55</span><span class="media thumb" role="img" aria-label="Rapper on stage in purple light" style="background:linear-gradient(135deg,#6a3ad0,#200a40)"></span></div>
    </div>
    <div class="abs scroll"><i></i></div>
  </section>

  <!-- mix -->
  <section>
    <div class="media mix-art" role="img" aria-label="Illustration of colourful cassette tapes with music notes"></div>
    <h2 class="abs mix-title">Mix</h2>
    <span class="rule mix-rule"></span>
    <div class="abs copy mix-copy">
      <p>Lorem ipsum dolor sit amet, consectetur adipiscing elit. Viverra eu cursus et tellus suscipit. A fames urna, mattis diam. Aliquam placerat lacus augue leo interdum id amet fringilla. Tempor sem purus pellentesque proin semper. Eget morbi odio donec pellentesque. Id vitae sit cras id sit. Nunc, quis dictumst non tellus posuere. Lorem ipsum dolor sit amet, consectetur adipiscing elit. Viverra eu cursus et tellus suscipit. A fames urna, mattis diam.</p>
      <p>Lorem ipsum dolor sit amet, consectetur adipiscing elit. Viverra eu cursus et tellus suscipit. A fames urna, mattis diam. Aliquam placerat lacus augue leo interdum id amet fringilla. Tempor sem purus pellentesque proin semper. Eget morbi odio donec pellentesque. Id vitae sit cras id sit. Nunc, quis dictumst non tellus posuere. Lorem ipsum dolor sit amet, consectetur adipiscing elit. Viverra eu cursus et tellus suscipit. A fames urna, mattis diam.</p>
    </div>
  </section>

  <!-- photos -->
  <section>
    <div class="media photos-bg" role="img" aria-label="Dim red brick wall backdrop"></div>
    <h2 class="abs h-section" style="top:2912px">Photos</h2>
    <span class="rule" style="left:412px;top:2960px"></span>
    <div class="photo" role="img" aria-label="DJ in a white shirt under yellow stage lights" style="left:43px;top:3008px;width:262px;height:297px;background:radial-gradient(ellipse at 60% 30%,#e8e04a 0%,#6a7a20 45%,#1a1a10 100%)"></div>
    <div class="photo" role="img" aria-label="Hand on a mixer in purple light" style="left:317px;top:3008px;width:251px;height:130px;background:linear-gradient(135deg,#4a2aa0,#1a0a40)"></div>
    <div class="photo" role="img" aria-label="Hands on a DJ controller" style="left:317px;top:3155px;width:251px;height:150px;background:linear-gradient(135deg,#6a6a70,#1a1a1e)"></div>
    <div class="photo" role="img" aria-label="DJ with headphones in red and blue light" style="left:597px;top:3008px;width:261px;height:297px;background:linear-gradient(160deg,#c0203a 0%,#5a2a8a 55%,#1a1030 100%)"></div>
  </section>

  <!-- shop -->
  <section>
    <span class="abs" style="left:388px;top:3457px;width:99px;height:1px;background:#777"></span>
    <div class="abs view-all">Viwe all <svg width="18" height="8" viewBox="0 0 18 8"><path d="M0 4 H16 M13 1 L16 4 L13 7" stroke="#fff" stroke-width="1" fill="none"/></svg></div>
    <div class="shirt" role="img" aria-label="White T-shirt with red and black print" style="left:32px;background:linear-gradient(180deg,#f4f4f4,#dcdcdc)"></div>
    <div class="shirt" role="img" aria-label="Black T-shirt with pink print" style="left:252px;background:linear-gradient(180deg,#2a2a2a,#111)"></div>
    <div class="shirt" role="img" aria-label="Grey T-shirt with black print" style="left:485px;background:linear-gradient(180deg,#a8a8a8,#8a8a8a)"></div>
    <div class="shirt" role="img" aria-label="White ringer T-shirt with record print" style="left:693px;background:linear-gradient(180deg,#f4f4f4,#dcdcdc)"></div>
    <div class="buy" style="left:32px"><span class="cart"><svg width="16" height="14" viewBox="0 0 16 14" fill="none" stroke="#fff" stroke-width="1.5"><path d="M1 1 H3 L5 9 H13 L14 3 H4"/><circle cx="6" cy="12" r="1"/><circle cx="12" cy="12" r="1"/></svg></span><span><b>Add to card</b><small>15.0$</small></span></div>
    <div class="buy" style="left:262px"><span class="cart"><svg width="16" height="14" viewBox="0 0 16 14" fill="none" stroke="#fff" stroke-width="1.5"><path d="M1 1 H3 L5 9 H13 L14 3 H4"/><circle cx="6" cy="12" r="1"/><circle cx="12" cy="12" r="1"/></svg></span><span><b>Add to card</b><small>15.0$</small></span></div>
    <div class="buy" style="left:492px"><span class="cart"><svg width="16" height="14" viewBox="0 0 16 14" fill="none" stroke="#fff" stroke-width="1.5"><path d="M1 1 H3 L5 9 H13 L14 3 H4"/><circle cx="6" cy="12" r="1"/><circle cx="12" cy="12" r="1"/></svg></span><span><b>Add to card</b><small>15.0$</small></span></div>
    <div class="buy" style="left:713px"><span class="cart"><svg width="16" height="14" viewBox="0 0 16 14" fill="none" stroke="#fff" stroke-width="1.5"><path d="M1 1 H3 L5 9 H13 L14 3 H4"/><circle cx="6" cy="12" r="1"/><circle cx="12" cy="12" r="1"/></svg></span><span><b>Add to card</b><small>15.0$</small></span></div>
  </section>

  <!-- newsletter -->
  <section class="abs newsletter">
    <span class="join">Join our</span>
    <span class="big">Newsletter</span>
    <span class="email">Enter you email</span>
    <span class="submit">SUBMIT</span>
  </section>

  <!-- footer -->
  <footer>
    <nav class="abs foot-nav"><span>Events</span><span>Livestream</span><span>Mixes</span><span class="gap">Playlists</span><span>Sign up</span><span class="gap">Photos</span><span>Bio</span><span class="gap">Shop</span></nav>
    <span class="abs foot-line"></span>
    <p class="abs copyright">Copyright 2021 Tarnish | All Right Reserver</p>
    <div class="abs social foot-social"><span>Facet</span><span>Chatly</span><span>Pixo</span><span>Chirp</span></div>
  </footer>

</main>
</body>
</html>
```